Product label for specialty fertilizer for cannabis

Create a label with our brand name and product information. The name of the new product is “Vardel” and the name is also the logo. The color palate is white/platinium/silver/shimmery. The product makes the flowers dense and hard so we want the logo to look strong and masculine. The liquid inside the bottle is white Which is what vardel means in Spanish
Also need a font for all the product information. See pics for example and
Target Market(s)
Cannabis growers
Industry/Entity Type
Cannabis
Colors
Designer to choose colors to be used in the design.
Requirements
Must have
- Strong visual presence for retail environment. Clean but bold look.
Nice to have
- Would be nice to have similar to a Tivo Mara font
Should not have
- Do not put any cannabis or marijuana images anywhere on the label

```html
<!DOCTYPE html>
<html lang="en">
<head>
<meta charset="utf-8">
<title>Vardel Specialty Fertilizer Label</title>
<link href="https://fonts.googleapis.com/css2?family=Oswald:wght@400;500;600&family=Roboto+Condensed:wght@400;700&display=swap" rel="stylesheet">
<style>
  :root {
    --page: #f2f2f2;
    --label-dark: #0f0f0f;
    --label-mid: #2a2a2a;
    --label-light: #4d4d4d;
    --silver: #d9d9d9;
    --silver-soft: #b8b8b8;
    --text: #e6e6e6;
    --smoke-blue: #5d7590;
  }
  * { margin: 0; padding: 0; box-sizing: border-box; }
  html, body { width: 1200px; height: 984px; overflow: hidden; background: var(--page); }
  .sheet { position: relative; width: 1200px; height: 984px; display: flex; gap: 40px; padding: 30px 40px; }
  .label {
    position: relative; flex: 1; height: 924px; overflow: hidden;
    background: linear-gradient(100deg, var(--label-dark) 0%, var(--label-mid) 55%, var(--label-light) 100%);
    color: var(--text);
    font-family: "Roboto Condensed", sans-serif;
  }
  .smoke {
    position: absolute; left: 10px; top: 130px; width: 520px; height: 380px;
    background: radial-gradient(ellipse at 55% 50%, rgba(93,117,144,0.55) 0%, rgba(93,117,144,0.2) 45%, rgba(0,0,0,0) 72%);
  }
  .brand {
    position: absolute; width: 100%; text-align: center;
    font-family: "Oswald", sans-serif; font-weight: 500; color: var(--silver);
  }
  .front .brand { top: 240px; font-size: 120px; letter-spacing: 4px; }
  .volume { position: absolute; top: 560px; width: 100%; text-align: center; font-family: "Oswald", sans-serif; font-size: 17px; color: var(--silver-soft); }
  .product-type { position: absolute; top: 590px; width: 100%; text-align: center; font-family: "Oswald", sans-serif; font-weight: 600; font-size: 50px; color: var(--silver); letter-spacing: 1px; }
  .rule { position: absolute; left: 0; right: 0; top: 690px; height: 4px; background: linear-gradient(90deg, #8a8a8a, #f4f4f4, #8a8a8a); }
  .tagline { position: absolute; top: 708px; width: 100%; text-align: center; font-family: "Oswald", sans-serif; font-weight: 500; font-size: 29px; color: var(--silver); }
  .back .brand { top: 150px; left: 20px; width: 220px; font-size: 52px; }
  .intro { position: absolute; top: 130px; left: 255px; width: 270px; font-size: 10.5px; line-height: 1.45; text-align: center; }
  .directions-title { position: absolute; top: 300px; left: 25px; font-size: 12px; font-weight: 700; color: var(--silver-soft); }
  .column { position: absolute; top: 330px; width: 235px; font-size: 10.5px; line-height: 1.45; }
  .column.left { left: 30px; color: var(--silver-soft); }
  .column.right { left: 290px; }
  .column h3 { font-size: 12.5px; font-weight: 700; color: var(--silver); margin-bottom: 3px; }
  .column p { margin-bottom: 14px; }
  .column .spacer { height: 40px; }
  .warning { position: absolute; top: 712px; width: 100%; text-align: center; font-family: "Oswald", sans-serif; font-weight: 500; font-size: 17.5px; color: var(--silver); }
</style>
</head>
<body>
<main class="sheet">
  <section class="label front">
    <div class="smoke" role="img" aria-label="Soft blue-grey smoke wisps behind the brand name"></div>
    <div class="brand">Vardel</div>
    <div class="volume">1 LITER</div>
    <div class="product-type">SPECIALTY FERTILIZER</div>
    <div class="rule"></div>
    <div class="tagline">MAKES THE FLOWERS DENSE AND HARD</div>
  </section>

  <section class="label back">
    <div class="brand">Vardel</div>
    <p class="intro">In a way that no other product on the market can match, Vardel is a product that has been specifically created to dramatically activate flower output.<br>With a rapid commencement of blooming and then the delivery of explosive mass with rapid daily weight increases throughout the whole flowering cycle, results are almost instantly apparent. Through improved plant absorption technology, this patented composition produces results.</p>
    <div class="directions-title">DIRECTIONS:</div>
    <div class="column left">
      <h3>Recirculating and Run to Waste Systems</h3>
      <p>For five to seven days, set plants in flower. Apply VARDEL for 7 days after plants reach the required height. Use VARDEL at a dosage of 1-2ML per litre (4-8ML per gallon) of prepared nutrition solution to hasten the beginning of blooming. Adapt TDS/PPM as necessary.</p>
      <p>Redose with VARDEL once more if you want to prepare a fresh batch of nutritional solution during the seven-day window. After the seven days are over, flush your system with fresh water and resume your usual nutrient feeding schedule.</p>
      <p>Repeat the above application rate for weeks 6 and 7 of your flowering cycle if you want to harden your blossoms even more. A more uniform effect will be produced by these lengthier treatments at lower dosages.</p>
    </div>
    <div class="column right">
      <h3>Soil/Sunshine Mix</h3>
      <p>When plants attain the correct height, administer VARDEL at a rate of 1-2 ml per litre (4-8 ml per gallon) of nutrient solution along with the present fertilizer used on feed days. Adapt TDS/PPM as necessary. After seven days, rinse the growing medium with new water.</p>
      <div class="spacer"></div>
      <h3>General Usage Tip:</h3>
      <p>Make sure there is 20–30% runoff at each feed in run-to-waste systems. A sufficient run off removes old nutrients from your growing media, making room for new, plant-available ones to replace them. Aggressive flowering is induced by diamond density. This feeding method aids in ensuring that your plant has access to the optimal nutrients to promote this growth.</p>
    </div>
    <div class="rule"></div>
    <div class="warning">WARNING: FOR ORNAMENTAL PLANT USE ONLY. KEEP OUT OF REACH OF CHILDREN</div>
  </section>
</main>
</body>
</html>
```